Hi,

Here are some thoughts on the book cover for The BRIGHT Vital Plan: A Restorative Wellness Path for Active Mothers and their Households.

To simplify this project I've uploaded some images (all images are of a vortex or swirl) that I would like to see the book cover design created with. I've also uploaded a set of "elements" that I would like to see incorporated into the vortex.

My vision is to have you infuse the smaller "elements" into the vortex so they look like they are caught in the vortex or swirling in the vortex.

I have upload an amateur example which I did but it shows the smaller elements dropped into the larger vortex image.

Please don't hesitate to write me with any questions you may have.

Thank you,

Gregor

Please.

Target Market(s)

Busy Women, both stay at home and career women

Industry/Entity Type

Health

Font styles to use
Serif
Sans Serif

Requirements
Must have
• vortex or swirl with circular elements infused

```html
<!DOCTYPE html>
<html lang="en">
<head>
<meta charset="utf-8">
<title>The BRIGHT Vital Plan – Book Cover</title>
<link rel="stylesheet" href="https://fonts.googleapis.com/css2?family=Jost:wght@600&family=PT+Serif:wght@700&family=Roboto:wght@700&display=swap">
<style>
  :root {
    --page-bg: #ffffff;
    --navy: #0a1a55;
    --royal: #1c1ee8;
    --violet: #8a2be8;
    --cyan: #27e0ee;
    --aqua-light: #9ff3f7;
    --green: #2fd97a;
    --deep: #071a4a;
    --white: #ffffff;
  }
  * { margin: 0; padding: 0; box-sizing: border-box; }
  html, body {
    width: 1200px; height: 957px; overflow: hidden;
    background: var(--page-bg);
  }
  .stage { position: relative; width: 1200px; height: 957px; }

  .book-cover {
    position: absolute; left: 311px; top: 108px;
    width: 577px; height: 740px; overflow: hidden;
    background: var(--royal);
    box-shadow: 3px 4px 8px rgba(0,0,0,0.35);
  }

  .cover-art {
    position: absolute; left: 0; top: 67px; width: 577px; height: 536px;
    background:
      radial-gradient(ellipse 30% 22% at 46% 48%, #bff6ff 0%, #49c8f0 45%, transparent 75%),
      radial-gradient(ellipse 55% 45% at 46% 50%, #2a9df2 0%, #1b3fe0 40%, transparent 70%),
      radial-gradient(ellipse 85% 70% at 50% 55%, #2ed9a8 0%, #1fbf63 35%, #0f4aa0 65%, var(--deep) 100%);
  }

  .band { position: absolute; }
  .band-top {
    left: 0; top: 0; width: 577px; height: 67px;
    background: linear-gradient(90deg, var(--violet) 0%, #3a1cf0 30%, var(--royal) 70%, #4a4ae8 100%);
  }
  .band-bottom {
    left: 0; top: 603px; width: 577px; height: 137px;
    background: linear-gradient(90deg, #3b7fe0 0%, #2fd8f0 20%, var(--cyan) 60%, #35e6c8 100%);
  }
  .column-left {
    left: 0; top: 0; width: 77px; height: 740px;
    background: rgba(60, 40, 230, 0.35);
  }
  .column-right {
    left: 505px; top: 0; width: 72px; height: 740px;
    background: rgba(150, 120, 255, 0.3);
  }
  .band-subtitle {
    left: 0; top: 410px; width: 577px; height: 90px;
    background: rgba(12, 20, 190, 0.7);
  }
  .title-veil {
    left: 77px; top: 67px; width: 428px; height: 343px;
    background: rgba(40, 60, 240, 0.28);
  }

  .book-title {
    position: absolute; left: 0; top: 104px; width: 577px;
    text-align: center;
    font-family: "Jost", sans-serif; font-weight: 600;
    font-size: 66px; line-height: 86px; letter-spacing: 0.5px;
    color: var(--white);
  }
  .book-title .accent { color: var(--aqua-light); }

  .book-subtitle {
    position: absolute; left: 0; top: 424px; width: 577px;
    text-align: center;
    font-family: "PT Serif", serif; font-weight: 700;
    font-size: 19px; line-height: 25px; letter-spacing: 0.6px;
    color: var(--white);
  }

  .book-authors {
    position: absolute; left: 0; top: 638px; width: 577px;
    text-align: center;
    font-family: "Roboto", sans-serif; font-weight: 700;
    font-size: 17px; line-height: 28px; letter-spacing: 1.5px;
    color: var(--navy);
  }
</style>
</head>
<body>
<main class="stage">
  <section class="book-cover">
    <div class="cover-art" role="img" aria-label="Swirling blue, cyan and green water vortex"></div>
    <div class="band title-veil"></div>
    <div class="band band-top"></div>
    <div class="band band-bottom"></div>
    <div class="band band-subtitle"></div>
    <div class="band column-left"></div>
    <div class="band column-right"></div>

    <h1 class="book-title">THE <span class="accent">BRIGHT</span><br>VITAL<br>PLAN:</h1>
    <p class="book-subtitle">A Restorative Wellness Path<br>for Active Mothers and their Households.</p>
    <p class="book-authors">Gregor T. Halden<br>Dr.Alan Verrick, MD</p>
  </section>
</main>
</body>
</html>
```